Real Estate Business Folders, Business Cards, Envelopes & Letterhead

Im looking for trendy, modern & professional design concepts for my business folder that will be used for real estate documents and property report presentations. I'm also looking for Business card designs, envelopes and letterhead with a similar theme. I have a logo already and I would like the logo colors to be incorporated in the design concepts.

Target Market(s)

Real Estate Investors, Banks, Financial Institutions

Industry/Entity Type

Real Estate

Colors
0455a3
959595
d3d3d3
848484

Requirements
Must have
• Trendy Modern, High Class look. Please include logo and colors and incorporate some silver or metallic.
• Business Address: 4812 Corvelle Blvd ste 210-300
• N. Las Vegas, NV 89084
• Phone: 702-555-0147
• Fax : 702-555-0183
• Email: info@mesacrestlandgroup.example
• Website: MesaCrestLandGroup.example

```html
<!DOCTYPE html>
<html lang="en">
<head>
<meta charset="utf-8">
<title>Mesa Crest Land Group – Stationery Set</title>
<link rel="stylesheet" href="https://fonts.googleapis.com/css2?family=Lora:wght@400;500&display=swap">
<style>
  :root {
    --brand-blue: #0455a3;
    --silver: #959595;
    --light-silver: #d3d3d3;
    --charcoal: #252525;
    --backdrop: #cbcbcb;
    --paper: #ffffff;
    --ink: #222222;
  }
  * { box-sizing: border-box; margin: 0; padding: 0; }
  html, body { width: 1200px; height: 1200px; overflow: hidden; }
  body { background: var(--backdrop); font-family: "Lora", Georgia, serif; color: var(--brand-blue); position: relative; }
  .sheet { position: absolute; background: var(--paper); overflow: hidden; }
  .corner-accent {
    position: absolute; top: 0; right: 0;
    background: linear-gradient(135deg, var(--light-silver) 0%, var(--silver) 45%, var(--brand-blue) 80%, var(--charcoal) 100%);
  }
  .brand { position: absolute; display: flex; align-items: center; gap: 7px; }
  .brand-mark { background: var(--brand-blue); flex: none; }
  .brand-name { font-weight: 400; color: var(--brand-blue); line-height: 1.02; letter-spacing: 0.02em; text-transform: uppercase; white-space: nowrap; }
  .icon { width: 1em; height: 1em; fill: var(--brand-blue); vertical-align: -0.12em; flex: none; }
  .contact-row { position: absolute; display: flex; align-items: center; white-space: nowrap; }
  .contact-row .item { display: flex; align-items: center; gap: 0.45em; }

  /* Business card front */
  .card-front { left: 162px; top: 258px; width: 288px; height: 173px; }
  .card-front .corner-accent { width: 128px; height: 40px; }
  .card-front .brand { left: 16px; top: 42px; }
  .card-front .brand-mark { width: 16px; height: 16px; }
  .card-front .brand-name { font-size: 15px; }
  .card-front .divider { position: absolute; left: 118px; top: 92px; width: 1.5px; height: 58px; background: var(--brand-blue); }
  .card-front .address { position: absolute; left: 145px; top: 101px; font-size: 7.3px; line-height: 12px; }
  .card-front .phones { position: absolute; left: 135px; top: 128px; font-size: 7px; line-height: 11px; }
  .card-front .phones div { display: flex; gap: 5px; align-items: center; }
  .card-front .contact-row { left: 16px; top: 157px; font-size: 6.4px; color: var(--ink); gap: 12px; }
  .card-front .contact-row .icon { fill: var(--ink); }

  /* Business card back */
  .card-back { left: 278px; top: 445px; width: 288px; height: 173px; }
  .card-back .corner-accent { width: 120px; height: 38px; }
  .card-back .brand { left: 0; right: 0; top: 68px; justify-content: center; gap: 10px; }
  .card-back .brand-mark { width: 28px; height: 28px; }
  .card-back .brand-name { font-size: 25px; }
  .card-back .band { position: absolute; left: 0; bottom: 0; width: 100%; height: 16px; background: var(--brand-blue); }
  .card-back .contact-row { left: 16px; bottom: 3px; font-size: 6.4px; color: #fff; gap: 12px; }
  .card-back .contact-row .icon { fill: #fff; }

  /* Envelope */
  .envelope { left: 162px; top: 638px; width: 403px; height: 288px; }
  .envelope .corner-accent { width: 190px; height: 60px; }
  .envelope .brand { left: 22px; top: 18px; }
  .envelope .brand-mark { width: 15px; height: 15px; }
  .envelope .brand-name { font-size: 14px; }
  .envelope .address { position: absolute; left: 27px; top: 162px; font-size: 9.3px; line-height: 18px; }
  .envelope .address .line { display: flex; align-items: center; gap: 6px; }
  .envelope .phone-line { font-size: 10px; margin-left: -2px; }
  .envelope .contact-row { left: 26px; top: 263px; font-size: 7.8px; color: var(--ink); gap: 16px; letter-spacing: 0.06em; }
  .envelope .contact-row .icon { fill: var(--ink); font-size: 10px; }

  /* Letterhead */
  .letterhead { left: 610px; top: 293px; width: 490px; height: 634px; }
  .letterhead .corner-accent { width: 230px; height: 70px; }
  .letterhead .brand { left: 21px; top: 22px; }
  .letterhead .brand-mark { width: 16px; height: 16px; }
  .letterhead .brand-name { font-size: 15px; }
  .letterhead .header-contact { left: 16px; top: 94px; font-size: 9.4px; gap: 12px; }
  .letterhead .header-contact .phone { font-size: 10.4px; }
  .letterhead .band { position: absolute; left: 0; bottom: 0; width: 100%; height: 38px; background: var(--brand-blue); }
  .letterhead .footer-contact { left: 16px; bottom: 10px; font-size: 9.6px; color: #fff; letter-spacing: 0.07em; width: 458px; justify-content: space-between; }
  .letterhead .footer-contact .icon { fill: #fff; font-size: 16px; }
</style>
</head>
<body>

<svg width="0" height="0" style="position:absolute" aria-hidden="true">
  <defs>
    <symbol id="icon-phone" viewBox="0 0 16 16"><path d="M4 1 L6 1 L7 5 L5 6.5 C6 9 7.5 10.5 9.5 11.5 L11 9.5 L15 10.5 L15 13 C15 14 14 15 13 15 C7 14.5 1.5 9 1 3 C1 2 2 1 4 1 Z"/></symbol>
    <symbol id="icon-fax" viewBox="0 0 16 16"><path d="M4 1 H12 V5 H4 Z M1 6 H15 V12 H12 V10 H4 V12 H1 Z M5 11 H11 V15 H5 Z"/></symbol>
    <symbol id="icon-mail" viewBox="0 0 16 12"><path d="M0 0 H16 V12 H0 Z M1.5 1.5 L8 7 L14.5 1.5 Z" fill-rule="evenodd"/></symbol>
    <symbol id="icon-globe" viewBox="0 0 16 16"><g fill="none" stroke="currentColor" stroke-width="1.2"><circle cx="8" cy="8" r="7"/><ellipse cx="8" cy="8" rx="3" ry="7"/><path d="M1 8 H15 M2.5 4.5 H13.5 M2.5 11.5 H13.5"/></g></symbol>
  </defs>
</svg>

<!-- Business card front -->
<section class="sheet card-front">
  <div class="corner-accent" role="img" aria-label="Decorative corner graphic in silver, blue and charcoal"></div>
  <div class="brand"><span class="brand-mark"></span><span class="brand-name">Mesa Crest<br>Land Group</span></div>
  <span class="divider"></span>
  <p class="address">4812 CORVELLE BLVD STE 210-300<br>N. LAS VEGAS, NV 89084</p>
  <div class="phones">
    <div><svg class="icon"><use href="#icon-phone"/></svg>702-555-0147</div>
    <div><svg class="icon"><use href="#icon-fax"/></svg>702-555-0183</div>
  </div>
  <div class="contact-row">
    <span class="item"><svg class="icon"><use href="#icon-mail"/></svg>info@mesacrestlandgroup.example</span>
    <span class="item"><svg class="icon" style="color:#222"><use href="#icon-globe"/></svg>www.MesaCrestLandGroup.example</span>
  </div>
</section>

<!-- Business card back -->
<section class="sheet card-back">
  <div class="corner-accent" role="img" aria-label="Decorative corner graphic in silver, blue and charcoal"></div>
  <div class="brand"><span class="brand-mark"></span><span class="brand-name">Mesa Crest<br>Land Group</span></div>
  <div class="band"></div>
  <div class="contact-row">
    <span class="item"><svg class="icon"><use href="#icon-mail"/></svg>info@mesacrestlandgroup.example</span>
    <span class="item"><svg class="icon" style="color:#fff"><use href="#icon-globe"/></svg>www.MesaCrestLandGroup.example</span>
  </div>
</section>

<!-- Envelope -->
<section class="sheet envelope">
  <div class="corner-accent" role="img" aria-label="Decorative corner graphic in silver, blue and charcoal"></div>
  <div class="brand"><span class="brand-mark"></span><span class="brand-name">Mesa Crest<br>Land Group</span></div>
  <div class="address">
    <div class="line">4812 CORVELLE BLVD STE 210-300</div>
    <div class="line">N. LAS VEGAS, NV 89084</div>
    <div class="line phone-line"><svg class="icon"><use href="#icon-phone"/></svg>702-555-0147</div>
    <div class="line phone-line"><svg class="icon"><use href="#icon-fax"/></svg>702-555-0183</div>
  </div>
  <div class="contact-row">
    <span class="item"><svg class="icon"><use href="#icon-mail"/></svg>info@mesacrestlandgroup.example</span>
    <span class="item"><svg class="icon" style="color:#222"><use href="#icon-globe"/></svg>www.MesaCrestLandGroup.example</span>
  </div>
</section>

<!-- Letterhead -->
<section class="sheet letterhead">
  <div class="corner-accent" role="img" aria-label="Decorative corner graphic in silver, blue and charcoal"></div>
  <div class="brand"><span class="brand-mark"></span><span class="brand-name">Mesa Crest<br>Land Group</span></div>
  <div class="contact-row header-contact">
    <span class="item">4812 CORVELLE BLVD STE 210-300 | N. LAS VEGAS, NV 89084</span>
    <span class="item phone"><svg class="icon"><use href="#icon-phone"/></svg>702-555-0147</span>
    <span class="item phone"><svg class="icon"><use href="#icon-fax"/></svg>702-555-0183</span>
  </div>
  <div class="band"></div>
  <div class="contact-row footer-contact">
    <span class="item"><svg class="icon" style="width:1.5em"><use href="#icon-mail"/></svg>info@mesacrestlandgroup.example</span>
    <span class="item"><svg class="icon" style="color:#fff"><use href="#icon-globe"/></svg>www.MesaCrestLandGroup.example</span>
  </div>
</section>

</body>
</html>
```